Gardener needs an exciting new flyer design.

I'm a passionate gardener that requires a custom flyer design for a owner operator gardening business. Design will be for a DL flyer. I'm based on the Sunshine coast in Queensland Australia. My target audience is the residential market on the Sunshine coast. Business name is Marlowe Greens. My services are, lawn mowing, weeding, Eco Friendly fertilizing, green waste removal, Mulching, tree and shrub pruning, Full garden makeovers, hedging, pressure cleaning, privacy screening, Timber deck rejuvenation, Planting, Turf preparation and installation, and much more. Free no obligation quotes, reliable and friendly service, great rates. 12 years experience. Web www.marlowegreens.com.au - Phone 0418527064 - Email doug@marlowegreens.com.au I would like the design to portray a friendly and professional approach.

Target Market(s)

Residential

Industry/Entity Type

Gardener

Font styles to use
Serif

Colors
9ccb3b
abd037
3176b5

Requirements
Must have
• my services, my logo, my contact details,

```html
<!DOCTYPE html>
<html lang="en">
<head>
<meta charset="utf-8">
<title>Marlowe Greens – DL Flyer</title>
<link rel="stylesheet" href="https://fonts.googleapis.com/css2?family=Lato:ital,wght@0,300;0,400;0,700;0,900;1,400&display=swap">
<style>
  :root {
    --green: #3d9a42;
    --green-dark: #2f7f35;
    --purple: #5b2160;
    --white: #ffffff;
    --ink: #222222;
    --backdrop: #e8e8eb;
  }
  * { box-sizing: border-box; margin: 0; padding: 0; }
  html, body { width: 1200px; height: 1200px; overflow: hidden; }
  body {
    background: var(--backdrop);
    font-family: "Lato", sans-serif;
    color: var(--ink);
    position: relative;
  }
  .flyer {
    position: absolute;
    left: 311px; top: 30px;
    width: 577px; height: 1140px;
    background: var(--white);
    overflow: hidden;
  }
  .contact {
    position: absolute; right: 34px; top: 54px;
    text-align: right; font-size: 17px; line-height: 21px; color: var(--ink);
    z-index: 2;
  }
  .contact-line { display: flex; justify-content: flex-end; align-items: center; gap: 6px; }
  .contact-line svg { width: 14px; height: 14px; }
  .brand {
    position: absolute; left: 36px; top: 160px;
    display: flex; align-items: center; gap: 9px;
    font-size: 25px; font-weight: 700; color: var(--green);
    z-index: 2;
  }
  .brand-dot { width: 15px; height: 15px; border-radius: 50%; background: var(--purple); }
  .hero { position: absolute; left: 0; top: 0; width: 577px; height: 640px; }
  .headline {
    position: absolute; left: 43px; top: 300px;
    color: var(--white); font-size: 28px; font-weight: 300; line-height: 39px;
    letter-spacing: 0.3px; z-index: 2;
  }
  .headline strong { font-weight: 700; }
  .pill {
    position: absolute; background: var(--green); color: var(--white);
    border-radius: 20px; font-weight: 700; font-size: 24px;
    display: flex; align-items: center; justify-content: center;
    height: 39px; width: 262px; left: 155px;
  }
  .pill-garden { top: 585px; }
  .pill-other { top: 855px; z-index: 2; }
  .service-list {
    position: absolute; left: 43px; top: 650px;
    list-style: none; font-size: 17px; line-height: 21.6px;
  }
  .tick { color: var(--green); font-weight: 700; margin-right: 7px; }
  .promise {
    position: absolute; left: 332px; top: 634px;
    width: 210px; height: 210px; border-radius: 50%;
    background: var(--purple); color: var(--white);
    display: flex; flex-direction: column; align-items: center; justify-content: center;
    text-align: center; font-size: 17px; line-height: 18px;
  }
  .promise-item { padding: 5px 0; width: 150px; }
  .promise-item + .promise-item { border-top: 1px solid rgba(255,255,255,0.6); }
  .other-box {
    position: absolute; left: 43px; top: 869px; width: 491px; height: 130px;
    border: 1.5px solid var(--green); border-bottom: none;
  }
  .other-list {
    position: absolute; left: 43px; top: 906px; width: 491px;
    text-align: center; font-size: 17px; line-height: 21.5px;
  }
  .other-list .tick { margin-right: 2px; }
  .other-list .gap { margin-left: 16px; }
  .call-band {
    position: absolute; left: 0; top: 980px; width: 577px; height: 160px;
    background: var(--green); color: var(--white); text-align: center;
  }
  .call-title { margin-top: 16px; font-size: 23px; font-weight: 400; letter-spacing: 0.3px; }
  .call-number {
    margin-top: 6px; font-size: 40px; font-weight: 900;
    display: flex; justify-content: center; align-items: center; gap: 6px;
  }
  .call-number svg { width: 34px; height: 34px; }
  .call-area { margin-top: 6px; font-size: 17px; }
</style>
</head>
<body>
  <main class="flyer">
    <svg class="hero" viewBox="0 0 577 640">
      <defs>
        <linearGradient id="lawnHouse" x1="0" y1="0" x2="0" y2="1">
          <stop offset="0" stop-color="#4c8fd4"/>
          <stop offset="0.3" stop-color="#a9b7b8"/>
          <stop offset="0.5" stop-color="#d9d4cb"/>
          <stop offset="0.62" stop-color="#5f9a2f"/>
          <stop offset="1" stop-color="#3f8a24"/>
        </linearGradient>
      </defs>
      <path d="M0,528 Q210,596 430,528 Q210,620 0,552 Z" fill="var(--purple)"/>
      <path d="M0,258 C90,228 210,236 270,262 L300,500 C220,556 90,556 0,522 Z" fill="var(--green)"/>
      <circle cx="440" cy="332" r="220" fill="var(--purple)"/>
      <circle cx="452" cy="322" r="209" fill="url(#lawnHouse)" role="img" aria-label="Photo of a white weatherboard home with a freshly striped green lawn under blue sky"/>
    </svg>

    <div class="contact">
      <div class="contact-line">
        <svg viewBox="0 0 14 14"><circle cx="7" cy="7" r="6" fill="none" stroke="var(--green)" stroke-width="1.2"/><path d="M1,7H13M7,1C4,4 4,10 7,13M7,1C10,4 10,10 7,13" fill="none" stroke="var(--green)" stroke-width="1"/></svg>
        <span>www.marlowegreens.com.au</span>
      </div>
      <div class="contact-line">
        <svg viewBox="0 0 14 14"><rect x="1" y="3" width="12" height="9" fill="var(--green)"/><path d="M1,3L7,8L13,3" fill="none" stroke="#fff" stroke-width="1.2"/></svg>
        <span>doug@marlowegreens.com.au</span>
      </div>
    </div>

    <div class="brand"><span class="brand-dot"></span><span>Marlowe Greens</span></div>

    <h1 class="headline">A BEAUTIFUL<br><strong>GARDEN</strong><br>DOESN'T<br>HAPPEN BY<br>ITSELF!</h1>

    <h2 class="pill pill-garden">GARDEN SERVICES</h2>
    <ul class="service-list">
      <li><span class="tick">✓</span>Lawn mowing</li>
      <li><span class="tick">✓</span>Turf preparation and installation</li>
      <li><span class="tick">✓</span>Tree and shrub pruning</li>
      <li><span class="tick">✓</span>Fertilizing</li>
      <li><span class="tick">✓</span>Full garden makeovers</li>
      <li><span class="tick">✓</span>Green waste removal</li>
      <li><span class="tick">✓</span>Garden mulching</li>
      <li><span class="tick">✓</span>Hedging</li>
      <li><span class="tick">✓</span>Weeding</li>
    </ul>

    <div class="promise">
      <div class="promise-item">✓ Free no<br>obligation quotes</div>
      <div class="promise-item">✓ Reliable and<br>friendly service</div>
      <div class="promise-item">✓ Great rates</div>
      <div class="promise-item">✓12 years<br>experience</div>
    </div>

    <div class="other-box"></div>
    <h2 class="pill pill-other">OTHER SERVICES</h2>
    <div class="other-list">
      <p><span class="tick">✓</span>Aluminium fencing and gate installation and repairs</p>
      <p><span class="tick">✓</span>Timber decking rejuvenation and repairs</p>
      <p><span class="tick">✓</span>Pressure cleaning <span class="gap"><span class="tick">✓</span>And much more!</span></p>
    </div>

    <section class="call-band">
      <p class="call-title">JUST A PHONE CALL AWAY</p>
      <p class="call-number">
        <svg viewBox="0 0 24 24"><path d="M6.6,10.8c1.4,2.8,3.8,5.1,6.6,6.6l2.2-2.2c0.3-0.3,0.7-0.4,1-0.2c1.1,0.4,2.3,0.6,3.6,0.6c0.6,0,1,0.4,1,1V20c0,0.6-0.4,1-1,1C10.6,21,3,13.4,3,4c0-0.6,0.4-1,1-1h3.5c0.6,0,1,0.4,1,1c0,1.3,0.2,2.5,0.6,3.6c0.1,0.3,0,0.7-0.2,1L6.6,10.8z" fill="#fff"/><path d="M14,3a7,7 0 0 1 7,7M14,6a4,4 0 0 1 4,4" fill="none" stroke="#fff" stroke-width="1.6"/></svg>
        <span>0418527064</span>
      </p>
      <p class="call-area">Servicing Noosa to Caloundra and everywhere in-between.</p>
    </section>
  </main>
</body>
</html>
```